Men’s hair skin and beard line

I own a men’s salon in Texas and are beginning to expand its market into the men’s retail line and already have it being manufactured out of the UK. It’s paraben free, vegan, sulphate free. I need a better brand look for the packaging. This script font is a bit hard to read. I want it masculine yet clean lines. All colors even gold or silver are welcomed. Bottle choices are silver canisters, white or black.

Target Market(s)

Men

Industry/Entity Type

Men’s hair skin and beard industry. Retail centers, high end barbers, and gyms

Font styles to use
Other font styles liked:
• Montserrat ,helvetica neue, or lato font

Colors
0054AA
0677BA
7BADD7
CADEEF
E8F1F8
0094D4
00A9DD
6FCCEA
C7EBF8
E9F6FB
00AB8E
00BBA5
67D7C9
C6EFE9
E9F9F6

Requirements
Must have
• Logo and name
Nice to have
• I’m open to all.
Should not have
• Not feminine

```html
<!DOCTYPE html>
<html lang="en">
<head>
<meta charset="UTF-8">
<title>Steadman Beard Oil – Label</title>
<link rel="stylesheet" href="https://fonts.googleapis.com/css2?family=Bebas+Neue&family=Poppins:wght@500;600;700&display=swap">
<style>
  :root {
    --backdrop-light: #b4b4b4;
    --backdrop-dark: #8f8f8f;
    --label-black: #0d0d0d;
    --label-charcoal: #1c1c1c;
    --gold-deep: #b4832a;
    --gold-mid: #d9b14c;
    --gold-light: #f6e49a;
    --gold-solid: #d6ae4c;
    --ink-white: #ffffff;
    --cream: #fbf5e8;
    --cream-shade: #e9e1cf;
    --ink-black: #111111;
    --gold-gradient: linear-gradient(90deg, var(--gold-deep) 0%, var(--gold-light) 28%, var(--gold-mid) 55%, var(--gold-light) 80%, var(--gold-deep) 100%);
  }
  * { margin: 0; padding: 0; box-sizing: border-box; }
  html, body { width: 835px; height: 1200px; overflow: hidden; }
  body {
    background: radial-gradient(ellipse at 50% 40%, var(--backdrop-light), var(--backdrop-dark));
    font-family: "Poppins", sans-serif;
    position: relative;
  }
  .label {
    position: absolute;
    left: 157px; top: 20px;
    width: 520px; height: 1160px;
    background: radial-gradient(ellipse at 60% 30%, var(--label-charcoal), var(--label-black) 70%);
    overflow: hidden;
  }
  .brand-mark {
    position: absolute; left: 50%; top: 170px;
    width: 54px; height: 54px; margin-left: -27px;
    background: var(--gold-solid);
  }
  .brand-name {
    position: absolute; left: 0; right: 0; top: 262px;
    text-align: center;
    font-weight: 600; font-size: 60px; letter-spacing: 1px; line-height: 1;
    color: var(--gold-solid);
  }
  .brand-tagline {
    position: absolute; left: 0; right: 0; top: 333px;
    display: flex; align-items: center; justify-content: center; gap: 12px;
    font-weight: 600; font-size: 19px; letter-spacing: 1.5px;
    color: var(--gold-solid);
  }
  .brand-tagline::before, .brand-tagline::after {
    content: ""; width: 24px; height: 2px; background: var(--gold-solid);
  }
  .art-area {
    position: absolute;
    background: linear-gradient(180deg, var(--cream), var(--cream-shade));
    border-radius: 6px;
  }
  .art-area.mustache { left: 155px; top: 403px; width: 208px; height: 48px; }
  .art-area.beard { left: 198px; top: 734px; width: 122px; height: 117px; }
  .product-name {
    position: absolute; left: 0; right: 0;
    text-align: center;
    font-family: "Bebas Neue", sans-serif;
    color: var(--ink-white);
    font-size: 164px; line-height: 1; letter-spacing: -2px;
    transform: scaleX(0.9);
  }
  .product-name.word-beard { top: 458px; }
  .product-name.word-oil { top: 588px; }
  .claim {
    position: absolute; left: 0; right: 0; top: 872px;
    display: flex; align-items: center; justify-content: center; gap: 8px;
    font-weight: 700; font-size: 20px; line-height: 1; color: var(--ink-white);
  }
  .claim .rule { display: flex; flex-direction: column; gap: 4px; }
  .claim .rule span { display: block; height: 1.5px; background: var(--ink-white); }
  .claim .rule.left span:first-child { width: 30px; margin-left: auto; }
  .claim .rule.left span:last-child { width: 48px; }
  .claim .rule.right span:first-child { width: 30px; }
  .claim .rule.right span:last-child { width: 48px; }
  .feature-bar {
    position: absolute; left: 85px; top: 902px;
    width: 349px; height: 52px;
    background: var(--gold-gradient);
    display: flex; align-items: center; justify-content: center;
    font-family: "Bebas Neue", sans-serif;
    font-size: 46px; line-height: 1; padding-top: 4px;
    color: var(--ink-black);
  }
  .feature-bar span { display: inline-block; transform: scaleX(0.84); white-space: nowrap; }
  .description {
    position: absolute; left: 0; right: 0; top: 964px;
    text-align: center;
    font-weight: 600; font-size: 11.2px; line-height: 14px;
    color: var(--ink-white);
  }
  .volume-tab {
    position: absolute; left: 138px; top: 1031px;
    width: 242px; height: 56px;
    background: var(--gold-gradient);
    border-radius: 12px 12px 0 0;
    display: flex; align-items: center; justify-content: center;
    font-weight: 700; font-size: 31px; color: var(--ink-black);
  }
  .volume-band {
    position: absolute; left: 47px; right: 0; top: 1085px;
    height: 37px;
    background: var(--gold-gradient);
  }
</style>
</head>
<body>
  <main class="label">
    <div class="brand-mark"></div>
    <h1 class="brand-name">STEADMAN</h1>
    <p class="brand-tagline">MEN’S FINE GROOMING</p>

    <div class="art-area mustache" role="img" aria-label="Cream mustache illustration"></div>
    <h2 class="product-name word-beard">BEARD</h2>
    <h2 class="product-name word-oil">OIL</h2>
    <div class="art-area beard" role="img" aria-label="Cream beard illustration"></div>

    <p class="claim">
      <span class="rule left"><span></span><span></span></span>
      100% NATURAL
      <span class="rule right"><span></span><span></span></span>
    </p>
    <div class="feature-bar"><span>MASCULINE FRAGRANCE</span></div>
    <p class="description">Lorem ipsum dolor sit amet, consectetur adipiscing elit,<br>sed do eiusmod tempor incididunt ut labore</p>

    <div class="volume-tab">30ml / 1fl.oz</div>
    <div class="volume-band"></div>
  </main>
</body>
</html>
```